Shop Front Design

We are Corrow Fusion Traders, a welding products suppliers just north of London.
We would like a banner 4.0m x 1.5m that will be placed above our building entrance to introduce our business to regular and new customers. Info we would like lister:
-Our Logo (CFT logo1)
-Core info: email address, phone number, opening hours
cftflame@mailvane.net
07412 508 391
Monday to Friday 12:00 - 18:00
Saturday 09:00 - 12:00
-Our core services:
Welders & Consumables
Hire
Industrial Gases
Training Courses
-Our core suppliers logos. I would like to see what impact they would have on the banner
Preferred colour theme orange and grey.

```html
<!DOCTYPE html>
<html lang="en">
<head>
<meta charset="utf-8">
<title>Corrow Fusion Traders – Shop Front Banner</title>
<link rel="stylesheet" href="https://fonts.googleapis.com/css2?family=Arimo:wght@400;700&display=swap">
<style>
  :root {
    --orange: #ee7623;
    --orange-deep: #f08a24;
    --grey: #77787b;
    --grey-dark: #6b6c6e;
    --grey-swoosh: #818286;
    --paper: #ffffff;
    --edge: #d4d4d4;
  }
  * { margin: 0; padding: 0; box-sizing: border-box; }
  html, body { width: 1200px; height: 450px; overflow: hidden; background: var(--paper); }
  .banner {
    position: relative;
    width: 1200px;
    height: 450px;
    background: var(--paper);
    border: 1px solid var(--edge);
    font-family: "Arimo", Arial, sans-serif;
    overflow: hidden;
  }
  .corner-swoosh { position: absolute; top: 0; left: 0; width: 1200px; height: 450px; }
  .brand {
    position: absolute;
    left: 118px;
    top: 170px;
    display: flex;
    align-items: center;
    gap: 18px;
  }
  .brand-dot {
    width: 58px;
    height: 58px;
    border-radius: 50%;
    background: var(--grey-dark);
    flex: none;
  }
  .brand-name {
    font-weight: 700;
    font-size: 42px;
    color: var(--orange-deep);
    letter-spacing: 0.5px;
    white-space: nowrap;
  }
  .divider {
    position: absolute;
    left: 724px;
    top: 120px;
    width: 4px;
    height: 184px;
    background: var(--grey-dark);
  }
  .services {
    position: absolute;
    left: 776px;
    top: 113px;
    list-style: none;
    font-size: 32px;
    line-height: 38px;
  }
  .services-title { color: var(--grey); }
  .service { color: var(--orange); }
  .contact {
    position: absolute;
    left: 0;
    top: 378px;
    width: 1200px;
    text-align: center;
    color: var(--grey);
    font-size: 22px;
    line-height: 28px;
  }
</style>
</head>
<body>
  <main class="banner">
    <svg class="corner-swoosh" viewBox="0 0 1200 450" aria-hidden="true">
      <path d="M1037,30 C1115,95 1165,155 1200,203 V124 C1140,80 1090,50 1037,30 Z" fill="var(--grey-swoosh)"/>
      <path d="M936,0 C970,8 1005,18 1037,30 C1090,50 1140,80 1200,124 V0 Z" fill="var(--orange)"/>
    </svg>

    <div class="brand">
      <span class="brand-dot"></span>
      <span class="brand-name">Corrow Fusion Traders</span>
    </div>

    <div class="divider"></div>

    <ul class="services">
      <li class="services-title">Our core services:</li>
      <li class="service">Welders &amp; Consumables</li>
      <li class="service">Hire</li>
      <li class="service">Industrial Gases</li>
      <li class="service">Training Courses</li>
    </ul>

    <div class="contact">
      <p>Email Address: cftflame@mailvane.net, Phone Number: 07412 508 391</p>
      <p>Monday to Friday 12:00 - 18:00, Saturday 09:00 - 12:00</p>
    </div>
  </main>
</body>
</html>
```